Write some Short Articles in Chinese using only 175 characters

DO NOT POST "I CAN DO VERY WELL CHINA LANGUAGE" AND OTHER NON-RESPONSIVE ADS! IF YOU CANNOT WRITE CHINESE, DO NOT WASTE EVERYONE'S TIME!!

ABSOLUTELY ***NO**** WEXLO RENDER OR OTHER MACHINE TRANSLATIONS. YES, I DO READ CHINESE AND CAN TELL THE DIFFERENCE.

Contest requires you to post a substantial portion of one complete article as a sample, in Chinese characters.

We need 100 very simple Chinese articles (1 - 2 paragraphs each, approximately 50-100 words) that talk about a wide variety of topics (all non-fiction) such as animals, computers, Internet, health, science, different countries, technology, famous people, inventions, travel, food, holidays, nutrition, etc. -- really any non-fiction topic. (You may choose any non-fiction topic, but please NO sexual or child-inappropriate content.) However, these articles are intended for adults who do not read Chinese well, so they must be limited to using only 175 Chinese characters (the list of acceptable characters will be provided). You may use up to five words or short phrases in each article that are outside of the 175 characters ("new words") and those new words should be underlined in the article. With these limitations, wee know these will not be elegant writing -- that is OK, but they must be grammatically correct and make sense in Chinese.

Prefer traditional characters if possible. Delivery to be in a Word file or RTF format, Unicode (UTF-8) encoding.

A sample article and the list of the 175 Chinese characters that may be used are attached.

```html
<!DOCTYPE html>
<html lang="zh-Hant">
<head>
<meta charset="utf-8">
<title>海南島 — 短文範例</title>
<link rel="stylesheet" href="https://fonts.googleapis.com/css2?family=Noto+Serif+TC:wght@400&family=Tinos:wght@400&display=swap">
<style>
  :root {
    --paper: #ffffff;
    --ink: #000000;
  }
  html, body {
    margin: 0;
    padding: 0;
    width: 1200px;
    height: 579px;
    overflow: hidden;
    background: var(--paper);
  }
  .sheet {
    position: relative;
    width: 1200px;
    height: 579px;
    background: var(--paper);
    color: var(--ink);
  }
  .article {
    position: absolute;
    left: 10px;
    top: 2px;
    margin: 0;
    font-family: "Noto Serif TC", "Songti TC", serif;
    font-size: 57px;
    line-height: 80px;
    white-space: nowrap;
    letter-spacing: 0;
  }
  .article .line { display: block; }
  .new-word {
    text-decoration: underline;
    text-decoration-thickness: 2px;
    text-underline-offset: 6px;
  }
  .note-ref {
    font-family: "Tinos", "Times New Roman", serif;
    font-size: 30px;
    vertical-align: 26px;
    line-height: 0;
    padding: 0 4px 0 3px;
  }
  .glossary {
    position: absolute;
    left: 112px;
    top: 418px;
    border-collapse: collapse;
    font-family: "Tinos", "Times New Roman", serif;
    font-size: 25px;
    line-height: 34px;
  }
  .glossary td { padding: 0; vertical-align: top; }
  .glossary .num { width: 42px; }
  .glossary .pinyin { width: 215px; }
  .glossary .equals { width: 160px; }
</style>
</head>
<body>
<main class="sheet">
  <p class="article">
    <span class="line"><span class="new-word">海南島</span><sup class="note-ref">1</sup>在中国的南部，雖然<span class="new-word">面積</span><sup class="note-ref">2</sup>不大，但</span>
    <span class="line">是很美，天氣也很好，大家都很喜歡到這裏</span>
    <span class="line">玩，所以這裏也叫中国的<span class="new-word">夏威夷</span><sup class="note-ref">3</sup>。因為這</span>
    <span class="line">裏車不多，空气也很好，所以<span class="new-word">晚上</span><sup class="note-ref">4</sup>可以看</span>
    <span class="line">到月亮和星星。</span>
  </p>

  <table class="glossary">
    <tr><td class="num">1</td><td class="pinyin">hǎi nán dǎo</td><td class="equals">=</td><td class="meaning">island</td></tr>
    <tr><td class="num">2</td><td class="pinyin">miàn jī</td><td class="equals">=</td><td class="meaning">area</td></tr>
    <tr><td class="num">3</td><td class="pinyin">xià wēi yí</td><td class="equals">=</td><td class="meaning">Hawaii</td></tr>
    <tr><td class="num">4</td><td class="pinyin">wǒn shang</td><td class="equals">=</td><td class="meaning">Evening</td></tr>
  </table>
</main>
</body>
</html>
```